Design Menu card and product signage within shop for Indian fast food outlet

we are Indian Cafe style shop based in Sydney called Spice Lantern street Food.
we sell Indian street food,tea,sweets and other fast food from the outlet

we will provide you pictures of few products with prices and size of banners/which will be displayed within shop inside to enhance and grab customer attraction

Target Market(s)

Indians and other communites all age group

Requirements
Must have
• pictures of Samosas, Panipuri,chaat , dosa,momos sweets can be included in menu
Nice to have
• Earthtone color schemes will be preferred and not too dark colors

```html
<!DOCTYPE html>
<html lang="en">
<head>
<meta charset="utf-8">
<title>Hot Snacks Menu</title>
<link href="https://fonts.googleapis.com/css2?family=Alegreya+Sans:ital,wght@1,400&family=Cinzel:wght@500&family=Open+Sans:ital,wght@1,400&display=swap" rel="stylesheet">
<style>
:root{
  --page:#ffffff;
  --paper:#f4f0ea;
  --rule:#8a8580;
  --gold:#d5b469;
  --badge:#5a5049;
  --badge-text:#f4efe6;
  --rust:#a4574a;
  --body:#4a4440;
  --stamp:#b5343a;
}
*{margin:0;padding:0;box-sizing:border-box}
html,body{width:1200px;height:849px;overflow:hidden;background:var(--page)}
.sheet{position:relative;width:1200px;height:849px}
.frame{position:absolute;left:20px;top:25px;width:1161px;height:799px;border:1px solid var(--rule)}
.panel{position:absolute;top:26px;height:797px;background:var(--paper)}
.panel--left{left:21px;width:443px}
.panel--right{left:601px;width:444px}
.gold-edge{position:absolute;top:26px;width:5px;height:797px;background:var(--gold)}
.photo{position:absolute}
.title-badge{position:absolute;width:178px;height:34px;background:var(--badge);border:1px solid var(--badge);outline:1px solid var(--badge);outline-offset:2px;
  color:var(--badge-text);font-family:"Cinzel",serif;font-size:15.5px;letter-spacing:.2px;display:flex;align-items:center;justify-content:center}
.ornament{position:absolute;width:44px;height:10px;background:linear-gradient(90deg,transparent,#9a928a,transparent);opacity:.55}
.item{position:absolute;width:380px}
.item__name{font-family:"Alegreya Sans",sans-serif;font-style:italic;font-size:17px;color:var(--rust);line-height:18px}
.item__desc{font-family:"Open Sans",sans-serif;font-style:italic;font-size:7.6px;color:var(--body);line-height:11px;margin-top:2px}
.item__desc svg{vertical-align:middle;margin-left:2px}
.price{position:absolute;font-family:"Alegreya Sans",sans-serif;font-style:italic;font-size:17px;color:var(--rust);line-height:20px}
.price small{font-size:10px}
.sketch{position:absolute;left:645px;top:628px;width:215px;height:140px;border-radius:50% 50% 8px 8px;background:radial-gradient(ellipse at center,#e2dcd2 0%,rgba(244,240,234,0) 70%)}
.stamp{position:absolute;left:808px;top:662px;width:92px;height:92px;border-radius:50%;border:4px solid var(--stamp);opacity:.8;transform:rotate(-18deg)}
</style>
</head>
<body>
<div class="sheet">
  <div class="frame"></div>

  <!-- left panel -->
  <div class="panel panel--left"></div>
  <div class="gold-edge" style="left:464px"></div>
  <div class="ornament" style="left:218px;top:62px" role="img" aria-label="decorative flourish"></div>
  <div class="title-badge" style="left:152px;top:85px">-HOT SNACKS MENU-</div>
  <div class="ornament" style="left:218px;top:129px" role="img" aria-label="decorative flourish"></div>

  <div class="item" style="left:67px;top:165px"><div class="item__name">Samosa</div><div class="item__desc">Fried pastry with a savoury filling made from<br>spiced potatoes and peas.<br>-No onions and garlic added <svg width="30" height="12" viewBox="0 0 30 12"><circle cx="13" cy="6" r="5" fill="none" stroke="#777" stroke-width=".8"/><line x1="4" y1="1" x2="28" y2="11" stroke="var(--stamp)" stroke-width="1"/></svg></div></div>
  <div class="price" style="left:370px;top:166px">$2.50 <small>(each)</small></div>

  <div class="item" style="left:67px;top:240px"><div class="item__name">Kachori</div><div class="item__desc">Fried pastry with a savoury filling made from lentils.<br>-No onions and garlic added <svg width="30" height="12" viewBox="0 0 30 12"><circle cx="13" cy="6" r="5" fill="none" stroke="#777" stroke-width=".8"/><line x1="4" y1="1" x2="28" y2="11" stroke="var(--stamp)" stroke-width="1"/></svg></div></div>
  <div class="price" style="left:370px;top:241px">$3.00 <small>(each)</small></div>

  <div class="item" style="left:67px;top:301px"><div class="item__name">Bread Pakora</div><div class="item__desc">Bread sandwiched with a savoury filling of potatoes and peas.<br>-No onions and garlic added <svg width="30" height="12" viewBox="0 0 30 12"><circle cx="13" cy="6" r="5" fill="none" stroke="#777" stroke-width=".8"/><line x1="4" y1="1" x2="28" y2="11" stroke="var(--stamp)" stroke-width="1"/></svg></div></div>
  <div class="price" style="left:370px;top:302px">$3.00 <small>(each)</small></div>

  <div class="item" style="left:67px;top:362px"><div class="item__name">Chilli Pakora</div><div class="item__desc">Long green chillies dipped in chickpea batter and fried.<br>-No onions and garlic added</div></div>
  <div class="price" style="left:370px;top:364px">$2.00 <small>(each)</small></div>

  <div class="item" style="left:67px;top:423px"><div class="item__name">Onion Pakora</div><div class="item__desc">Onion sliced, dipped in chickpea batter<br>and fried to golden brown.</div></div>
  <div class="price" style="left:370px;top:424px">$5.00 <small>(plate)</small></div>

  <div class="item" style="left:67px;top:484px"><div class="item__name">Medhu Vada</div><div class="item__desc">South Indian fritter made from white urid lentil, usually made in<br>a doughnut shape, with a crispy exterior and soft interior.</div></div>
  <div class="price" style="left:370px;top:486px">$2.50 <small>(each)</small></div>

  <div class="item" style="left:67px;top:545px"><div class="item__name">Masala Vada</div><div class="item__desc">Patties made by coarsely grinding soaked chana dal or<br>bengal gram (lentils) with spices, onions &amp; herbs.</div></div>
  <div class="price" style="left:370px;top:547px">$2.00 <small>(each)</small></div>

  <div class="item" style="left:67px;top:606px"><div class="item__name">Aloo Bonda</div><div class="item__desc">Ball shaped fritters with a coating of chickpea batter filled<br>in with spiced potatoes.</div></div>
  <div class="price" style="left:370px;top:608px">$2.00 <small>(each)</small></div>

  <div class="item" style="left:67px;top:667px"><div class="item__name">Paneer Puff</div><div class="item__desc">Pastry Turnovers with a flaky golden crust with spicy<br>flavourful paneer (cottage cheese ) filling.</div></div>
  <div class="price" style="left:370px;top:669px">$4.00 <small>(each)</small></div>

  <div class="item" style="left:67px;top:728px"><div class="item__name">Veg Roll</div><div class="item__desc">Spring rolls filled with mix vegetables and coated with<br>breadcrumbs for crispy golden coloured fried snacks</div></div>
  <div class="price" style="left:370px;top:730px">$3.00 <small>(each)</small><br>$5.00 <small>(for 2)</small></div>

  <div class="photo" style="left:469px;top:26px;width:131px;height:132px;background:linear-gradient(160deg,#b8352c,#d9a660 55%,#e9e1d3)" role="img" aria-label="Photo of samosas with mint chutney"></div>
  <div class="photo" style="left:469px;top:158px;width:131px;height:132px;background:linear-gradient(150deg,#c9b79b,#d7a66a 50%,#a9784a)" role="img" aria-label="Photo of kachori pastries on a board"></div>
  <div class="photo" style="left:469px;top:290px;width:131px;height:198px;background:linear-gradient(160deg,#e7c08a,#c9874a 40%,#2f2a26 65%,#4d86b1)" role="img" aria-label="Photo of bread pakora with chillies and lemon"></div>
  <div class="photo" style="left:469px;top:488px;width:131px;height:192px;background:linear-gradient(170deg,#d17a2c,#b9541f 55%,#e8ddd0)" role="img" aria-label="Photo of onion pakora fritters"></div>
  <div class="photo" style="left:469px;top:680px;width:131px;height:143px;background:linear-gradient(160deg,#2b2624,#c58a3a 45%,#e8e3dc)" role="img" aria-label="Photo of aloo bonda fritters"></div>

  <!-- right panel -->
  <div class="panel panel--right"></div>
  <div class="gold-edge" style="left:1044px"></div>
  <div class="ornament" style="left:799px;top:62px" role="img" aria-label="decorative flourish"></div>
  <div class="title-badge" style="left:733px;top:85px">-HOT SNACKS MENU-</div>
  <div class="ornament" style="left:799px;top:129px" role="img" aria-label="decorative flourish"></div>

  <div class="item" style="left:648px;top:165px"><div class="item__name">Chicken Roll</div><div class="item__desc">Spring rolls filled with minced chicken and spices, coated<br>with breadcrumbs for crispy golden coloured fried snacks</div></div>
  <div class="price" style="left:950px;top:166px">$3.00 <small>(each)</small><br>$5.00 <small>(for 2)</small></div>

  <div class="item" style="left:648px;top:226px"><div class="item__name">Lamb Roll</div><div class="item__desc">Spring rolls filled with minced lamb, spices and coated with<br>breadcrumbs for crispy golden coloured fried snacks</div></div>
  <div class="price" style="left:950px;top:227px">$3.00 <small>(each)</small><br>$5.00 <small>(for 2)</small></div>

  <div class="item" style="left:648px;top:286px"><div class="item__name">Vada Pav</div><div class="item__desc">Deep fried potato dumpling placed inside a bread bun/pav.<br>Perfect Mumbai side dish!</div></div>
  <div class="price" style="left:950px;top:287px">$5.99 <small>(each)</small></div>

  <div class="item" style="left:648px;top:346px"><div class="item__name">Dabeli</div><div class="item__desc">It is a sweet &amp; savoury snack made by mixing boiled potatoes,<br>peanuts placed inside a bread bun/pav.</div></div>
  <div class="price" style="left:950px;top:347px">$5.99 <small>(each)</small></div>

  <div class="sketch" role="img" aria-label="Line sketch of samosas with a chutney bowl"></div>
  <div class="stamp" role="img" aria-label="Round stamp badge"></div>

  <div class="photo" style="left:1049px;top:26px;width:131px;height:166px;background:linear-gradient(150deg,#e0a060,#c47a3e 50%,#7a4a2a)" role="img" aria-label="Photo of chicken rolls"></div>
  <div class="photo" style="left:1049px;top:192px;width:131px;height:218px;background:linear-gradient(160deg,#6a8f3a,#d59a55 40%,#b86a32 70%,#c9a23c)" role="img" aria-label="Photo of lamb spring rolls"></div>
  <div class="photo" style="left:1049px;top:410px;width:131px;height:204px;background:linear-gradient(170deg,#c4a066,#efd9ae 45%,#e4ded8)" role="img" aria-label="Photo of vada pav buns"></div>
  <div class="photo" style="left:1049px;top:614px;width:131px;height:209px;background:linear-gradient(160deg,#4a3b32,#e6a351 45%,#c4682f 75%,#2e2624)" role="img" aria-label="Photo of dabeli buns with sev and pomegranate"></div>
</div>
</body>
</html>
```